GravaLoop. Customer needs to know about us, what services we provide & contact us

We are a waste tire recycling company. Our primary focus is on providing a sustainable and cost effective service focusing on: Waste Tire Management, Hassle Free Scheduling for Tire Collection, Mobile Shredding & Special site cleanup services. GravaLoop will be producing TDF, Clean Tire Wire & further materials.
Please look at https://harvonrubber.example
Please look at https://quelbamaterials.example

This is the look and feel of what we want

I have attached a word document with our website info.

Target Market(s)

Tire Install Companies. Such as morbanhaul.example. TDF Purchasers such as pelkofuel.example.

Industry/Entity Type

Waste Tire Recycling

Coding

Coded - Design and coding required

Number of Pages Required

3 page

Font styles to use
Other font styles liked:
• Look at our logo

Requirements
Must have
• We need a 3 page setup for About Us, Services & Contact Us. Contact us should be a form them can fill out and submit to us Images that are related to waste tire recycling. Clean, modern, innovative.
Nice to have
• The color and feel of the website should work with our logo that we did with artpivot
Should not have
• Anything progressive, political or "woke"

```html
<!DOCTYPE html>
<html lang="en">
<head>
<meta charset="utf-8">
<title>GravaLoop – Waste Tire Recycling</title>
<link href="https://fonts.googleapis.com/css2?family=Poppins:wght@400;500;600;700;800&display=swap" rel="stylesheet">
<style>
:root{
  --green:#17994a;
  --green-dark:#0f7a39;
  --green-light:#2bb35e;
  --ink:#1d1d1d;
  --muted:#666;
  --paper:#ffffff;
  --mist:#f2f3f2;
  --footer:#121212;
  --line:#d9d9d9;
}
*{margin:0;padding:0;box-sizing:border-box}
html,body{width:1200px;height:3328px;overflow:hidden}
body{font-family:'Poppins',sans-serif;color:var(--ink);background:var(--paper);position:relative}
.abs{position:absolute}

/* hero */
.hero{position:absolute;left:0;top:0;width:1200px;height:980px;overflow:hidden}
.hero-photo{position:absolute;inset:0;background:linear-gradient(180deg,#6f8796 0%,#a9b7bd 38%,#b9a58a 60%,#7c6a55 78%,#4a4037 100%)}
.hero-shade{position:absolute;inset:0;background:linear-gradient(180deg,rgba(0,0,0,.35),rgba(0,0,0,.1) 40%,rgba(0,0,0,.25))}
.nav{position:absolute;top:30px;left:0;width:1200px;height:40px}
.nav-links{position:absolute;left:116px;top:10px;display:flex;gap:30px;font-size:15px;color:#fff}
.nav-links .active{color:var(--green-light)}
.brand{position:absolute;left:490px;top:0;display:flex;align-items:center;gap:10px;font-size:28px;font-weight:700;color:#fff}
.brand .dot{width:30px;height:30px;border-radius:50%;background:var(--green)}
.nav-phone{position:absolute;left:752px;top:10px;font-size:15px;color:#fff;display:flex;gap:8px;align-items:center}
.nav-search{position:absolute;left:940px;top:8px}
.btn{display:inline-block;background:var(--green);color:#fff;font-weight:600;border-radius:30px;text-align:center}
.nav-login{position:absolute;left:990px;top:0;width:92px;height:40px;line-height:40px;font-size:15px}
.hero-copy{position:absolute;left:0;top:160px;width:1200px;text-align:center;color:#fff}
.hero-copy .kicker{font-size:34px;font-weight:500;letter-spacing:2px}
.hero-copy h1{font-size:82px;font-weight:800;letter-spacing:3px;line-height:1;margin-top:10px}
.hero-copy p{font-size:16px;line-height:24px;width:460px;margin:16px auto 0}
.hero-copy .btn{margin-top:40px;width:150px;height:44px;line-height:44px;font-size:15px}
.arrow{position:absolute;top:300px}

/* section titles */
.title{position:absolute;left:0;width:1200px;text-align:center;font-size:34px;font-weight:700;letter-spacing:1px}
.title span{color:var(--green)}

/* services */
.cards{position:absolute;left:112px;top:812px;display:flex;gap:16px}
.card{width:232px;height:396px;background:#fff;box-shadow:0 6px 20px rgba(0,0,0,.12);position:relative;text-align:center}
.card-photo{height:168px}
.card-icon{position:absolute;left:86px;top:138px;width:60px;height:60px;border-radius:50%;background:var(--green);display:flex;align-items:center;justify-content:center;border:4px solid #fff}
.card h3{margin-top:48px;font-size:17px;font-weight:600;line-height:24px;height:52px}
.card p{font-size:13px;color:var(--muted);line-height:20px;margin:14px 20px 0}
.card .more{display:block;margin-top:14px;color:var(--green);font-size:14px;font-weight:600}

/* about */
.about{position:absolute;left:0;top:1300px;width:1200px;height:488px;background:linear-gradient(135deg,var(--green-light),var(--green-dark))}
.about-visual{position:absolute;left:150px;top:40px;width:410px;height:410px;border-radius:50%;background:radial-gradient(circle,#4a4a4a 0%,#2b2b2b 55%,rgba(255,255,255,.25) 56%,rgba(255,255,255,.08) 70%,transparent 71%)}
.about-copy{position:absolute;left:600px;top:95px;width:480px;color:#fff}
.about-copy h2{font-size:34px;font-weight:700;letter-spacing:1px}
.about-copy p{font-size:14px;line-height:24px;margin-top:20px}
.about-copy .btn{background:#fff;color:var(--green);margin-top:30px;width:150px;height:44px;line-height:44px;font-size:15px}

/* provide */
.provide{position:absolute;left:112px;top:1960px;width:976px;height:368px;display:flex}
.provide-photo{width:488px;height:368px;background:linear-gradient(180deg,#9fb3c2 0%,#c9d3d8 30%,#8a7a66 60%,#3d352e 100%)}
.provide-panel{width:488px;height:368px;background:linear-gradient(135deg,var(--green-light),var(--green-dark));color:#fff;display:flex;align-items:center;justify-content:center;text-align:center;font-size:28px;font-weight:500;line-height:42px}

/* contact */
.contact{position:absolute;left:0;top:2420px;width:1200px;height:588px;background:linear-gradient(180deg,#fff,var(--mist))}
.contact h2{position:absolute;left:112px;top:70px;font-size:34px;font-weight:700;letter-spacing:1px}
.contact h2 span{color:var(--green)}
.field{position:absolute;background:#fff;border:1px solid var(--line);border-radius:3px;font-size:13px;color:#999;padding:14px 16px}
.submit{position:absolute;left:112px;top:2872px;width:136px;height:44px;line-height:44px;font-size:15px}
.bin{position:absolute;left:680px;top:2500px;width:420px;height:480px;border-radius:24px;background:linear-gradient(180deg,#2a2a2a 0%,#3a3a3a 32%,#7fd36b 33%,#4fb64a 100%)}

/* footer */
.footer{position:absolute;left:0;top:3008px;width:1200px;height:320px;background:var(--footer);color:#fff}
.footer .brand{position:absolute;left:112px;top:66px;font-size:30px}
.socials{position:absolute;left:112px;top:150px;display:flex;gap:14px}
.socials span{width:30px;height:30px;border-radius:50%;background:var(--green)}
.fcol{position:absolute;top:60px;font-size:14px;line-height:26px}
.fcol h4{font-size:17px;font-weight:600;margin-bottom:12px;letter-spacing:.5px}
.fcol .row{display:flex;gap:10px;align-items:flex-start;margin-bottom:10px}
.copyright{position:absolute;left:0;top:272px;width:1200px;text-align:center;font-size:13px;color:#ccc}
</style>
</head>
<body>

<section class="hero">
  <div class="hero-photo" role="img" aria-label="Photo of stacked used truck tires on open dry ground under a cloudy sky"></div>
  <div class="hero-shade"></div>

  <nav class="nav">
    <div class="nav-links"><span class="active">Home</span><span>About Us</span><span>Services</span><span>Contact Us</span></div>
    <div class="brand"><span class="dot"></span>GravaLoop</div>
    <div class="nav-phone">
      <svg width="16" height="16" viewBox="0 0 24 24" fill="#fff"><path d="M6.6 10.8a15 15 0 0 0 6.6 6.6l2.2-2.2c.3-.3.7-.4 1-.2 1.1.4 2.3.6 3.6.6.6 0 1 .4 1 1V20c0 .6-.4 1-1 1A17 17 0 0 1 3 4c0-.6.4-1 1-1h3.5c.6 0 1 .4 1 1 0 1.3.2 2.5.6 3.6.1.3 0 .7-.2 1z"/></svg>
      +1 (555) 014 2290
    </div>
    <svg class="nav-search" width="22" height="22" viewBox="0 0 24 24" fill="none" stroke="#fff" stroke-width="2.4"><circle cx="10" cy="10" r="7"/><path d="M15 15l6 6"/></svg>
    <span class="btn nav-login">LOG IN</span>
  </nav>

  <div class="hero-copy">
    <div class="kicker">WELCOME TO</div>
    <h1>GRAVALOOP</h1>
    <p>Sustainable, cost effective tire recycling for your business, from pickup to processing and beyond.</p>
    <span class="btn">GET STARTED</span>
  </div>

  <svg class="arrow" style="left:60px" width="24" height="40" viewBox="0 0 24 40"><path d="M20 4L4 20l16 16" fill="none" stroke="#fff" stroke-width="4"/></svg>
  <svg class="arrow" style="left:1116px" width="24" height="40" viewBox="0 0 24 40"><path d="M4 4l16 16L4 36" fill="none" stroke="#fff" stroke-width="4"/></svg>

  <svg class="abs" style="left:0;top:840px" width="1200" height="140" viewBox="0 0 1200 140" preserveAspectRatio="none">
    <path d="M0 40 Q600 170 1200 40 L1200 140 L0 140Z" fill="var(--green)"/>
    <path d="M0 70 Q600 190 1200 70 L1200 140 L0 140Z" fill="#fff"/>
  </svg>
</section>

<h2 class="title" style="top:712px">OUR <span>SERVICES</span></h2>

<div class="cards">
  <article class="card">
    <div class="card-photo" role="img" aria-label="Photo of a pile of waste tires" style="background:linear-gradient(180deg,#555,#1f1f1f)"></div>
    <div class="card-icon"><svg width="28" height="28" viewBox="0 0 24 24" fill="none" stroke="#fff" stroke-width="2"><circle cx="12" cy="12" r="9"/><circle cx="12" cy="12" r="4"/></svg></div>
    <h3>Waste<br>Tire Management</h3>
    <p>Lorem ipsum dolor sit amet, consectetur adipis elit magna</p>
    <span class="more">Learn more</span>
  </article>
  <article class="card">
    <div class="card-photo" role="img" aria-label="Photo of shredded tire chips" style="background:linear-gradient(180deg,#8a8a8a,#444)"></div>
    <div class="card-icon"><svg width="28" height="28" viewBox="0 0 24 24" fill="none" stroke="#fff" stroke-width="2"><rect x="4" y="5" width="16" height="15" rx="2"/><path d="M4 10h16M9 3v4M15 3v4"/></svg></div>
    <h3>Hassle Free Scheduling<br>for Tire Collection</h3>
    <p>Lorem ipsum dolor sit amet, consectetur adipis elit magna</p>
    <span class="more">Learn more</span>
  </article>
  <article class="card">
    <div class="card-photo" role="img" aria-label="Photo of steel shredder blades" style="background:linear-gradient(180deg,#d8d8d8,#7d7d7d)"></div>
    <div class="card-icon"><svg width="28" height="28" viewBox="0 0 24 24" fill="none" stroke="#fff" stroke-width="2"><rect x="5" y="3" width="14" height="18" rx="2"/><path d="M9 8h6M9 12h6M9 16h6"/></svg></div>
    <h3>Mobile<br>Shredding</h3>
    <p>Lorem ipsum dolor sit amet, consectetur adipis elit magna</p>
    <span class="more">Learn more</span>
  </article>
  <article class="card">
    <div class="card-photo" role="img" aria-label="Photo of red site cleanup machinery" style="background:linear-gradient(180deg,#b7413a,#3a2a2a)"></div>
    <div class="card-icon"><svg width="28" height="28" viewBox="0 0 24 24" fill="none" stroke="#fff" stroke-width="2"><path d="M12 3v10M7 8l5 5 5-5M4 20h16"/></svg></div>
    <h3>Special site<br>cleanup services</h3>
    <p>Lorem ipsum dolor sit amet, consectetur adipis elit magna</p>
    <span class="more">Learn more</span>
  </article>
</div>

<section class="about">
  <div class="about-visual" role="img" aria-label="Photo of a stack of used tires inside a circular frame"></div>
  <div class="about-copy">
    <h2>ABOUT US</h2>
    <p>Lorem ipsum dolor sit amet, consectetur adipiscing elit, sed do eiusmod tempor incididunt ut labore et dolore magna aliqua. Ut enim ad minim veniam, quis nostrud exercitation ullamco laboris nisi ut aliquip ex ea commodo consequat. Duis aute irure dolor in reprehenderit in voluptate velit esse cillum dolore eu fugiat nulla pariatur. Excepteur sint occaecat cupidatat non proident, sunt in culpa qui officia deserunt mollit anim id est laborum.</p>
    <span class="btn">LEARN MORE</span>
  </div>
</section>

<h2 class="title" style="top:1856px">WE <span>PROVIDE</span></h2>

<div class="provide">
  <div class="provide-photo" role="img" aria-label="Photo of large piles of tires stored under a warehouse roof"></div>
  <div class="provide-panel">Clean Tire Wire &amp;<br>further materials</div>
</div>

<section class="contact">
  <h2>CONTACT <span>US</span></h2>
</section>
<div class="field" style="left:112px;top:2562px;width:224px;height:50px">First Name</div>
<div class="field" style="left:348px;top:2562px;width:232px;height:50px">Last Name</div>
<div class="field" style="left:112px;top:2642px;width:224px;height:50px">Email</div>
<div class="field" style="left:348px;top:2642px;width:232px;height:50px">Phone</div>
<div class="field" style="left:112px;top:2718px;width:468px;height:112px">Message</div>
<span class="btn submit">SUBMIT</span>
<div class="bin" role="img" aria-label="Illustration of used tires stacked in a green recycling bin"></div>

<footer class="footer">
  <div class="brand"><span class="dot"></span>GravaLoop</div>
  <div class="socials"><span></span><span></span><span></span><span></span></div>

  <div class="fcol" style="left:448px">
    <h4>QUICK LINKS</h4>
    <div>Home</div><div>About Us</div><div>Services</div><div>Contact Us</div>
  </div>

  <div class="fcol" style="left:660px;width:230px">
    <h4>CONTACT</h4>
    <div class="row"><svg width="14" height="18" viewBox="0 0 24 30" fill="#fff"><path d="M12 0a10 10 0 0 0-10 10c0 8 10 20 10 20s10-12 10-20A10 10 0 0 0 12 0zm0 14a4 4 0 1 1 0-8 4 4 0 0 1 0 8z"/></svg><span style="line-height:20px">Lorem ipsum dolor sit amet, consectetur adipiscing</span></div>
    <div class="row"><svg width="14" height="14" viewBox="0 0 24 24" fill="#fff" style="margin-top:6px"><path d="M6.6 10.8a15 15 0 0 0 6.6 6.6l2.2-2.2c.3-.3.7-.4 1-.2 1.1.4 2.3.6 3.6.6.6 0 1 .4 1 1V20c0 .6-.4 1-1 1A17 17 0 0 1 3 4c0-.6.4-1 1-1h3.5c.6 0 1 .4 1 1 0 1.3.2 2.5.6 3.6.1.3 0 .7-.2 1z"/></svg>+1 (555) 014 2290</div>
    <div class="row"><svg width="14" height="12" viewBox="0 0 24 18" fill="none" stroke="#fff" stroke-width="2" style="margin-top:7px"><rect x="1" y="1" width="22" height="16"/><path d="M1 1l11 9 11-9"/></svg>info@gravaloop.example</div>
  </div>

  <div class="fcol" style="left:960px">
    <h4>COMPANY</h4>
    <div>Terms &amp; Conditions</div><div>Privacy Policy</div><div>About Us</div><div>Support</div>
  </div>

  <div class="copyright">Copyright ©2022 GravaLoop. All Rights Reserved.</div>
</footer>

</body>
</html>
```